Stationery & business cards for nonprofit
WELL Wells of kindness beyond measure
Stationery & business cards for nonprofit - Religion and Spirituality
Creative Brief
Use same font as used in my logo
Ruth Pelling
President
481 Orchard Lane Birmingham, AL 35187
ruth@wellkb.org
www.wellkb.org
We are open to ideas and suggestions using our logo, this is a nonprofit that supports an orphanage and assists widows in Africa, as shown in the earth tone in the logo. Logo information: Font: Desire (manipulated), Swiss Condensed, Times Roman Color: Pantone 1395, Pantone 7407, Pantone 364 Our website is currently under development, but you can see pictures, etc to get a feel for our nonprofit by going to www.wellkb.org
We are thinking to put just the logo on the back of the card with the name (wells of kindness beyond measure) and the verse listed - I John 3:16-18
mirabelcostow mirabelcostow
AI and EPS file formats have been uploaded for use as needed.

```html
<!DOCTYPE html>
<html lang="en">
<head>
<meta charset="utf-8">
<title>WELL Business Card</title>
<link href="https://fonts.googleapis.com/css2?family=Exo+2:wght@400;500;600;700&display=swap" rel="stylesheet">
<style>
  :root {
    --backdrop: #3b3b3d;
    --card: #ffffff;
    --green: #2f7a1f;
    --gold: #a9801f;
    --ink: #2b2b2b;
    --muted: #4a4a4a;
  }
  * { margin: 0; padding: 0; box-sizing: border-box; }
  html, body {
    width: 1200px; height: 828px; overflow: hidden;
    background: var(--backdrop);
    font-family: "Exo 2", sans-serif;
  }
  .business-card {
    position: absolute; left: 100px; top: 128px;
    width: 1000px; height: 572px;
    background: var(--card);
    border-radius: 44px;
  }
  .brand {
    position: absolute; left: 640px; top: 70px;
    display: flex; align-items: center; gap: 18px;
  }
  .brand-dot {
    width: 46px; height: 46px; border-radius: 50%;
    background: var(--gold);
  }
  .brand-name {
    font-size: 92px; font-weight: 700; color: var(--green);
    letter-spacing: 4px; line-height: 1;
  }
  .rule {
    position: absolute; height: 4px; background: var(--gold);
  }
  .rule-top { left: 118px; top: 200px; width: 460px; }
  .rule-bottom { left: 60px; top: 306px; width: 420px; }
  .identity {
    position: absolute; left: 60px; top: 218px;
    display: flex; align-items: center; gap: 20px;
  }
  .icon-badge {
    width: 44px; height: 44px; border-radius: 50%;
    background: var(--green);
    display: flex; align-items: center; justify-content: center;
    flex-shrink: 0;
  }
  .icon-badge svg { width: 24px; height: 24px; fill: #fff; }
  .person-name {
    font-size: 26px; font-weight: 500; color: var(--ink);
    letter-spacing: 2px; text-transform: uppercase; line-height: 1.1;
  }
  .person-role {
    font-size: 21px; color: var(--green); letter-spacing: 3px;
    margin-top: 4px;
  }
  .contacts {
    position: absolute; left: 60px; top: 334px;
    list-style: none;
  }
  .contact-row {
    display: flex; align-items: flex-start; gap: 20px;
    margin-bottom: 14px;
  }
  .contact-row .icon-badge { width: 38px; height: 38px; }
  .contact-row .icon-badge svg { width: 20px; height: 20px; }
  .contact-text {
    font-size: 21px; color: var(--muted); letter-spacing: 1.5px;
    line-height: 1.25; padding-top: 4px;
  }
</style>
</head>
<body>
  <div class="business-card">
    <div class="brand">
      <span class="brand-dot"></span>
      <span class="brand-name">WELL</span>
    </div>

    <div class="rule rule-top"></div>

    <div class="identity">
      <span class="icon-badge">
        <svg viewBox="0 0 24 24"><circle cx="12" cy="8" r="4.5"/><path d="M3.5 21c0-4.7 3.8-7.5 8.5-7.5s8.5 2.8 8.5 7.5z"/></svg>
      </span>
      <div>
        <div class="person-name">Owen Marsh</div>
        <div class="person-role">Managing Director</div>
      </div>
    </div>

    <div class="rule rule-bottom"></div>

    <ul class="contacts">
      <li class="contact-row">
        <span class="icon-badge">
          <svg viewBox="0 0 24 24"><rect x="6" y="2" width="12" height="20" rx="2.5"/><rect x="8" y="5" width="8" height="12" fill="#2f7a1f"/></svg>
        </span>
        <span class="contact-text">012 555 0147<br>012 555 0147</span>
      </li>
      <li class="contact-row">
        <span class="icon-badge">
          <svg viewBox="0 0 24 24"><rect x="3" y="5" width="18" height="14" rx="1.5"/><path d="M4 6.5l8 6 8-6" stroke="#2f7a1f" stroke-width="2" fill="none"/></svg>
        </span>
        <span class="contact-text">owen@wellkb.org<br>www.wellkb.org</span>
      </li>
      <li class="contact-row">
        <span class="icon-badge">
          <svg viewBox="0 0 24 24"><path d="M12 2a7 7 0 0 0-7 7c0 5.2 7 13 7 13s7-7.8 7-13a7 7 0 0 0-7-7z"/><circle cx="12" cy="9" r="2.6" fill="#2f7a1f"/></svg>
        </span>
        <span class="contact-text">204.12th floor,Hill Crest<br>Road Dunmore</span>
      </li>
    </ul>
  </div>
</body>
</html>
```